Bref créative
Fjellbrinken Tannregulering Stationery
Orthodontic Clinic
Professional
Fjellbrinken Tannregulering
Kjeveortoped Stian Haugvik
Myrbakkvegen 128
Postboks 71 Kvernvika
5912 BERGEN
post@smilbrink.no
www.smilbrink.no
Telefon 55 83 17 62

```html
<!DOCTYPE html>
<html lang="no">
<head>
<meta charset="utf-8">
<title>Fjellbrinken Tannregulering – visittkort</title>
<link href="https://fonts.googleapis.com/css2?family=Arimo:wght@400;700&display=swap" rel="stylesheet">
<style>
  :root {
    --page-bg: #ffffff;
    --brand-blue: #1f86c9;
    --brand-blue-light: #35b3e8;
    --brand-navy: #1d3d8c;
    --brand-green: #8dc63f;
    --brand-green-dark: #4c9a2a;
    --text-grey: #3a4a5a;
    --white: #ffffff;
  }
  html, body {
    margin: 0;
    padding: 0;
    width: 1200px;
    height: 730px;
    overflow: hidden;
    background: var(--page-bg);
    font-family: "Arimo", Arial, sans-serif;
  }
  .sheet { position: relative; width: 1200px; height: 730px; }
  .card {
    position: absolute;
    width: 554px;
    height: 322px;
    overflow: hidden;
    box-shadow: 0 0 0 1px #d9dde2;
  }
  /* Front card */
  .card--front { left: 43px; top: 38px; background: var(--white); }
  .card--front .wave { position: absolute; left: 0; top: 0; }
  .brand-mark {
    position: absolute;
    display: flex;
    align-items: center;
    gap: 10px;
  }
  .brand-mark .dot {
    width: 30px; height: 30px; border-radius: 50%;
    background: var(--brand-blue);
    flex: none;
  }
  .brand-mark .name {
    font-weight: 700;
    font-size: 22px;
    line-height: 1.05;
    color: var(--brand-blue);
    text-transform: uppercase;
  }
  .card--front .brand-mark { left: 28px; top: 34px; }
  .front-info {
    position: absolute;
    right: 24px;
    top: 150px;
    text-align: right;
    color: var(--text-grey);
  }
  .front-info .clinic { font-size: 20px; color: var(--text-grey); margin: 0; }
  .front-info .doctor { font-size: 13px; color: var(--brand-blue); margin: 3px 0 0; }
  .front-info .contact { font-size: 12px; line-height: 1.55; margin: 18px 0 0; }

  /* Blue back card */
  .card--blue {
    left: 619px; top: 38px;
    background: linear-gradient(90deg, var(--brand-blue-light) 0%, var(--brand-blue) 50%, var(--brand-navy) 100%);
  }
  .card--blue .brand-mark { left: 0; right: 0; top: 108px; justify-content: center; }
  .card--blue .brand-mark .dot,
  .card--green .brand-mark .dot { background: var(--white); width: 26px; height: 26px; }
  .card--blue .brand-mark .name,
  .card--green .brand-mark .name { color: var(--white); font-size: 20px; }
  .blue-info {
    position: absolute; left: 0; right: 0; top: 222px;
    text-align: center; color: var(--white);
    font-size: 14px; line-height: 1.5;
  }
  .blue-info p { margin: 0; }

  /* Green back card */
  .card--green {
    left: 324px; top: 389px;
    background: radial-gradient(ellipse at 50% 40%, var(--brand-green) 0%, #72b236 55%, var(--brand-green-dark) 100%);
  }
  .card--green .brand-mark { left: 0; right: 0; top: 124px; justify-content: center; }
  .green-info {
    position: absolute; left: 0; right: 0; bottom: 28px;
    text-align: center; color: var(--white); font-size: 13px; margin: 0;
  }
</style>
</head>
<body>
<main class="sheet">

  <section class="card card--front" aria-label="Visittkort forside">
    <svg class="wave" width="554" height="322" viewBox="0 0 554 322" aria-hidden="true">
      <defs>
        <linearGradient id="waveFill" x1="0" y1="0" x2="1" y2="0">
          <stop offset="0" stop-color="#1f86c9"/>
          <stop offset="1" stop-color="#35b3e8"/>
        </linearGradient>
      </defs>
      <path d="M0 322 V248 C60 208 140 192 180 212 C205 226 214 285 220 322 Z" fill="url(#waveFill)"/>
      <path d="M0 322 V280 C70 248 140 238 170 252 C188 262 194 300 196 322 Z" fill="#ffffff" opacity="0.18"/>
    </svg>
    <div class="brand-mark">
      <span class="dot"></span>
      <span class="name">Fjellbrinken<br>Tannregulering</span>
    </div>
    <div class="front-info">
      <p class="clinic">Fjellbrinken Tannregulering</p>
      <p class="doctor">Kjeveortoped Stian Haugvik</p>
      <p class="contact">
        Myrbakkvegen 128, Postboks 71 Kvernvika, 5912 BERGEN<br>
        Phone: 55 83 17 62 | Fax: 55 91 40 27<br>
        Email: post@smilbrink.no
      </p>
    </div>
  </section>

  <section class="card card--blue" aria-label="Visittkort bakside blå">
    <div class="brand-mark">
      <span class="dot"></span>
      <span class="name">Fjellbrinken</span>
    </div>
    <div class="blue-info">
      <p>Fjellbrinken Tannregulering</p>
      <p>Telefon 55 83 17 62</p>
      <p>www.smilbrink.no</p>
    </div>
  </section>

  <section class="card card--green" aria-label="Visittkort bakside grønn">
    <div class="brand-mark">
      <span class="dot"></span>
      <span class="name">Fjellbrinken</span>
    </div>
    <p class="green-info">Fjellbrinken Tannregulering | Telefon 55 83 17 62 | www.smilbrink.no</p>
  </section>

</main>
</body>
</html>
```